New Hotel Showcase Website

We plan to launch a website called www.fernlodgings.net which showcases the world’s best new hotels. We want a mock up for 2 pages: the homepage (page 1) and the individual hotel page (page 2). We are looking for a design which combines simplicity while highlighting images/features of the hotel. Because the theme of the site is new hotels it is important that the design somehow emphasizes the age of each hotel listed – both on the homepage and then on the individual hotel page.

NOTE: WE WANT A CREATIVE, NEW APPROACH TO DISPLAYING HOTELS. NOT JUST A COPY OF CURRENT HOTEL WEBSITES.

The design should consider unique and creative ways of helping users to navigate the homepage (page 1) based on the age, location or style of the hotel they are interested in. The individual hotel page(page 2) can be more standard by clearly setting out hotel photos, feature lists, reviews, contact details and potential discounts. There is no booking system needed as this is not a hotel booking website.

The design should ideally be compatible with a content management system such as Page Forge. In terms of reference materials we like sites similar to:

http://www.quillwanderer.net
http://www.bobandkayporter.net
http://www.craftinns.net
http://www.pebblestays.net

These sites are designed far more simply than large booking sites such as www.voyaro.net, www.roomsy.net or even jaunt ledger. However, we are not looking for a copy of the above. We are looking for a design that presents hotels in a novel way and would be seen by the industry as a unique way of displaying new hotels.
Updates

Dear Designers - we have received quite a few entries already. Thank you. However, none of the designs submitted have responded to our brief. They are all copies or derivatives of current hotel websites which is not what we are looking for. We want (a) a new and creative approach to a hotel website and (b) one which creatively uses the age of the hotel (ie. 1 month old, 6 months old etc).

It will require creative thinking and new ideas. We wanted to challenge designers to come up with something new. Thanks.

```html
<!DOCTYPE html>
<html lang="en">
<head>
<meta charset="utf-8">
<title>Fernlodgings – Prague Hotel Lumen</title>
<link href="https://fonts.googleapis.com/css2?family=Open+Sans:ital,wght@0,400;0,600;1,400&family=Ubuntu:wght@400&display=swap" rel="stylesheet">
<style>
:root{
  --page-bg:#ffffff;
  --sheet:#f6f8fc;
  --dark:#2b2b2b;
  --panel-grey:#8b8b8b;
  --panel-line:#6f6f6f;
  --brand-blue:#0b56c9;
  --soft-blue:#4f8ae0;
  --tab-grey:#8a8a8a;
  --text:#222;
  --muted:#7a7a7a;
  --rule:#c4c4c4;
  --card-line:#c9ccd2;
}
*{margin:0;padding:0;box-sizing:border-box}
html,body{width:1090px;height:1200px;overflow:hidden;background:var(--page-bg)}
body{font-family:"Open Sans",sans-serif;color:var(--text);position:relative}
.sheet{position:absolute;left:89px;top:0;width:912px;height:1200px;background:var(--sheet);border-left:1px solid #e3e5ea;border-right:1px solid #e3e5ea}
.site-header{position:absolute;left:0;top:0;width:912px;height:94px;background:var(--dark)}
.menu-toggle{position:absolute;left:26px;top:56px;width:28px;height:24px}
.menu-toggle span{display:block;height:4px;background:#8d8d8d;margin-bottom:4px}
.wordmark{position:absolute;left:0;width:912px;top:26px;text-align:center;font-family:"Ubuntu",sans-serif;font-size:41px;letter-spacing:1px;color:#fff;line-height:48px}
.white-band{position:absolute;left:0;top:94px;width:912px;height:26px;background:#fff}
.hero{position:absolute;left:0;top:120px;width:912px;height:339px;background:linear-gradient(180deg,#d98a3c 0%,#c2742f 22%,#7c5a3c 48%,#4d4537 72%,#2f3a33 100%)}
.hero-next{position:absolute;left:872px;top:279px}
.search-panel{position:absolute;left:0;top:94px;width:223px}
.search-row{height:53px;background:var(--panel-grey);border-bottom:1px solid var(--panel-line);display:flex;align-items:center;padding:0 19px 0 21px;font-size:18px;color:#fff}
.search-row label{margin-right:8px}
.search-row .field{flex:1;height:27px;background:#fff;border-radius:3px}
.search-btn{height:54px;background:var(--brand-blue);color:#fff;font-size:18px;display:flex;align-items:center;justify-content:center;letter-spacing:.3px}
.title-row{position:absolute;left:24px;top:479px;display:flex;align-items:flex-start;white-space:nowrap}
.hotel-title{font-size:27px;letter-spacing:-1px;font-weight:400;line-height:36px}
.age-tag{position:relative;color:#fff;font-size:15px;line-height:20px;padding:2px 10px;border-radius:4px;transform:rotate(8deg);top:2px}
.age-tag.months{margin-left:26px;background:var(--brand-blue);z-index:1}
.age-tag.kind{margin-left:-4px;background:var(--soft-blue)}
.intro{position:absolute;left:27px;top:531px;width:566px;font-size:15.6px;letter-spacing:-.15px;line-height:19.2px;color:var(--muted)}
.intro p+p{margin-top:19px}
.divider{position:absolute;left:27px;top:862px;width:561px;height:1px;background:var(--rule)}
.features-heading{position:absolute;left:27px;top:877px;font-size:18px;font-weight:400}
.features{position:absolute;top:914px;list-style:none;font-size:16px;line-height:19.3px;color:var(--muted)}
.features.left{left:27px}
.features.right{left:301px}
.info-card{position:absolute;left:628px;width:284px;border:1px solid var(--card-line);border-radius:4px;background:#fff}
.contact-card{top:485px;height:170px}
.tabs{display:flex;height:45px}
.tab{flex:1;color:#fff;font-size:19px;padding:12px 0 0 19px;letter-spacing:.3px}
.tab.active{background:var(--soft-blue)}
.tab.idle{background:var(--tab-grey)}
.contact-body{padding:18px 0 0 19px;font-size:14px;line-height:19.3px}
.contact-body h3{font-size:14px;font-weight:600;margin-bottom:6px}
.contact-grid{display:grid;grid-template-columns:122px auto}
.contact-grid a{color:var(--text)}
.reviews-card{top:682px;height:252px}
.card-head{height:44px;background:var(--soft-blue);color:#fff;font-size:19px;padding:12px 0 0 19px;border-radius:3px 3px 0 0;letter-spacing:.3px}
.review{position:relative;padding-left:31px;margin-top:22px;width:245px}
.review q{display:block;font-style:italic;font-size:13.6px;line-height:19.3px;quotes:none;padding-right:6px}
.review q::before{content:"\201C";position:absolute;left:19px;top:-4px;font-style:normal;font-size:17px}
.review cite{display:block;text-align:right;font-style:normal;font-size:12.5px;color:var(--muted);margin-top:4px}
.review+.review{margin-top:16px}
.share{position:absolute;left:670px;top:962px;display:flex;gap:10px}
.share span{width:29px;height:29px;display:block}
.site-footer{position:absolute;left:0;top:1141px;width:912px;height:59px;background:var(--dark);color:#9a9a9a;font-size:11.5px;text-align:center;line-height:59px}
</style>
</head>
<body>
<div class="sheet">
  <header class="site-header">
    <div class="menu-toggle" aria-label="Menu"><span></span><span></span><span></span></div>
    <div class="wordmark">FERNLODGINGS</div>
  </header>
  <div class="white-band"></div>
  <div class="hero" role="img" aria-label="Sunset view over Prague rooftops, the river and its stone bridges"></div>
  <svg class="hero-next" width="22" height="22" viewBox="0 0 22 22" aria-label="Next photo">
    <circle cx="11" cy="11" r="10" fill="#fff"/>
    <path d="M8 6 L16 11 L8 16 Z" fill="var(--brand-blue)"/>
  </svg>
  <form class="search-panel">
    <div class="search-row"><label>Age:</label><span class="field"></span></div>
    <div class="search-row"><label>Location:</label><span class="field"></span></div>
    <div class="search-row"><label>Style:</label><span class="field"></span></div>
    <div class="search-btn">SEARCH HOTELS</div>
  </form>

  <div class="title-row">
    <h1 class="hotel-title">PRAGUE HOTEL LUMEN</h1>
    <span class="age-tag months">1 month</span>
    <span class="age-tag kind">design</span>
  </div>

  <div class="intro">
    <p>Lorem ipsum dolor sit amet, consectetur adipiscing elit. Maecenas vulputate magna in sem commodo, ut semper turpis mattis. Integer commodo erat accumsan libero vestibulum posuere. Sed sit amet augue pulvinar; tempor lectus ut, blandit purus! Pellentesque habitant morbi tristique senectus et netus et malesuada fames ac turpis egestas. Donec leo velit, imperdiet nec viverra a, vehicula ac ipsum. Donec et lorem erat. In hac habitasse platea dictumst. In pharetra lacus accumsan est ultricies, ut consectetur sem blandit. Nam blandit sollicitudin vulputate! Duis quis lacinia eros.</p>
    <p>Nam adipiscing tellus vitae consectetur egestas. Etiam lobortis bibendum libero eget tincidunt. Mauris molestie eleifend nisi vel pretium. Aliquam vel mi nec massa lobortis rutrum at vel mi. Vestibulum ante ipsum primis in faucibus orci luctus et ultrices posuere cubilia Curae; Curabitur non lobortis nisl, sit amet ultricies enim. Maecenas diam augue, semper sit amet gravida eget, varius eget nisi. Integer ullamcorper aliquet metus, nec suscipit orci ultricies sit amet.</p>
  </div>
  <div class="divider"></div>
  <h2 class="features-heading">Features</h2>
  <ul class="features left">
    <li>Lounge</li><li>Luggage storage</li><li>Multi-lingual staff</li><li>No pets allowed</li><li>Restaurant</li><li>Shopping area nearby</li><li>Spa</li><li>Spa treatments (on request)</li><li>Yoga</li>
  </ul>
  <ul class="features right">
    <li>100% non-smoking hotel</li><li>Babysitting (on request)</li><li>Bar</li><li>Bicycle rentals nearby</li><li>Free parking</li><li>Free wi-fi</li><li>Garden</li><li>Library</li><li>24 hour medical assistance</li>
  </ul>

  <section class="info-card contact-card">
    <div class="tabs"><div class="tab active">Contact</div><div class="tab idle">Map</div></div>
    <div class="contact-body">
      <h3>Prague Hotel Lumen</h3>
      <div class="contact-grid">
        <span>Lipova 412/7</span><span>info@hotellumen.cz</span>
        <span>Praha 1, 110 00</span><span>+420 555 018 274</span>
        <span>Czech republic</span><a href="#">www.hotellumen.cz</a>
      </div>
    </div>
  </section>

  <section class="info-card reviews-card">
    <div class="card-head">Reviews</div>
    <div class="review"><q>Very comfortable, great service and beautiful view!</q><cite>Marta Delvaux</cite></div>
    <div class="review"><q>Lovely atmosphere in the centre of Prague with everything you need on your holidays.</q><cite>Pavel Orrin</cite></div>
  </section>

  <div class="share" aria-label="Share">
    <span style="background:#3b5a9a"></span>
    <span style="background:#2aa3e6"></span>
    <span style="background:#e4502a"></span>
    <span style="background:#35465c"></span>
    <span style="background:#d0202a"></span>
  </div>

  <footer class="site-footer">Fernlodgings.net All rights reserved © 2013</footer>
</div>
</body>
</html>
```